Beachfront Boutique Hotel Web Design
Pelora Sands Belize Hotel Website Design
Beachfront Boutique Hotel Web Design - Hospitality Industry
Creative Brief
Hospitality Industry
Pelora Sands is located only fifty feet or so from the breathtaking Caribbean Sea on the tranquil island of Caye Caulker Belize with individual one-bedroom suites tastefully decorated to blend in with the island atmosphere. Each fully air-conditioned unit features either a king-sized bed or 2 queen-sized beds, private bath hot/cold water living room area cable flat screen TV, kitchenette and each has its own spacious deck space. Our ultra spacious units each with a approx. 500 sq ft of inside space makes them the most spacious yet affordable vacation units on the island. Warm furnishings make them a home away from home. This is the premier property on Caye Caulker. Come enjoy our breezy verandahs and starlit nights in relaxed comfort. Welcome to a beautiful island escape. These are beachfront condos that are among the best on the island. Step out from your deck and walk on the beach!
Like... Fun, whimsical, relaxing, chillax, simple, colorful, beachy, funky, flash, eye-catching, unique Dislike... Dull, difficult, complicated, busy, plain, standard, boring, blah
Fun
Teal, hot pink, orange, lime green, yellow, blue
https://photoshare.example-albums.com/582093746105829374610/PeloraSands?authkey=Tq8zLmWpR3vXnB7yH2dKcE
sociallink.example.com/PeloraSands
brindlecoveretreat.com
Link 1 is Fotalo album with logo, artwork and possible mock up. Link 2 is the Chatterly page for the hotel Link 3 is a website I like the general look of. Need the following headings: Beachfront Suites Rates & Reservations Gallery All About Caye Caulker Contact Us Need links to CH, Quipster and RoamRater widget. Would like flash... possible changing wallpaper (beach theme) and moving/flash heading/link/buttons :)

```html
<!DOCTYPE html>
<html lang="en">
<head>
<meta charset="utf-8">
<title>Pelora Sands Beach Suites – Caye Caulker, Belize</title>
<link href="https://fonts.googleapis.com/css2?family=Kalam:wght@400&family=PT+Sans:wght@400;700&family=PT+Sans+Narrow:wght@700&display=swap" rel="stylesheet">
<style>
  :root {
    --teal: #3cb8c9;
    --teal-light: #8fd6df;
    --teal-dark: #1e98ab;
    --lime: #9cc93a;
    --orange: #ef7d22;
    --pink: #ec4f8c;
    --yellow: #f6d34a;
    --sand: #f1e2c2;
    --sand-dark: #e2cfa6;
    --text: #7a6a55;
    --white: #ffffff;
  }
  * { box-sizing: border-box; margin: 0; padding: 0; }
  html, body { width: 1200px; height: 1027px; overflow: hidden; }
  body {
    position: relative;
    font-family: "PT Sans", sans-serif;
    background:
      repeating-linear-gradient(90deg, rgba(255,255,255,0.12) 0 2px, transparent 2px 60px),
      linear-gradient(180deg, var(--sand) 0%, #f4e8cd 50%, var(--sand-dark) 100%);
  }
  a { text-decoration: none; }
  .top-band { position: absolute; left: 0; top: 0; width: 1200px; height: 30px; background: var(--teal-light); }
  .brand {
    position: absolute; left: 153px; top: 26px; width: 196px; height: 190px;
    background: #d9c296; border: 3px solid #c9ad7b;
    display: flex; flex-direction: column; align-items: center; justify-content: center; gap: 8px;
  }
  .brand-mark { width: 34px; height: 34px; background: var(--teal); }
  .brand-name { font-family: "PT Sans", sans-serif; font-weight: 700; font-size: 29px; line-height: 1.05; color: var(--pink); text-align: center; }
  .social { position: absolute; left: 893px; top: 10px; display: flex; gap: 8px; }
  .social a {
    width: 40px; height: 40px; border-radius: 50%; background: #cdbb98; border: 2px solid var(--white);
    display: flex; align-items: center; justify-content: center;
    font-size: 12px; font-weight: 700; color: var(--white);
  }
  .call { position: absolute; left: 885px; top: 78px; color: var(--teal); font-family: "PT Sans Narrow", sans-serif; font-weight: 700; font-size: 25px; line-height: 1.15; }
  .main-nav { position: absolute; left: 362px; top: 180px; display: flex; gap: 8px; }
  .main-nav a {
    display: flex; align-items: center; justify-content: center; text-align: center;
    height: 44px; color: var(--white);
    font-family: "PT Sans Narrow", sans-serif; font-weight: 700; font-size: 13px; line-height: 1.05;
    text-transform: uppercase; border-radius: 4px 4px 0 0; box-shadow: 0 2px 3px rgba(0,0,0,0.15);
  }
  .nav-suites { width: 134px; background: var(--teal); }
  .nav-rates { width: 120px; background: var(--lime); }
  .nav-gallery { width: 125px; background: var(--orange); }
  .nav-caye { width: 125px; background: var(--pink); }
  .nav-contact { width: 128px; background: var(--teal); }
  .slider-accent { position: absolute; left: 800px; top: 600px; width: 260px; height: 70px; background: var(--teal); transform: rotate(-1deg); }
  .slider-frame {
    position: absolute; left: 153px; top: 228px; width: 890px; height: 432px;
    background: var(--white); padding: 14px; transform: rotate(-0.6deg);
    box-shadow: 0 4px 10px rgba(0,0,0,0.2);
  }
  .slider-photo { width: 100%; height: 100%; background: linear-gradient(180deg, #5aa7e0 0%, #3f8fd0 35%, #e34a7a 55%, #8fc23f 75%, #d9d0b8 100%); }
  .arrow { position: absolute; top: 404px; width: 40px; height: 64px; }
  .arrow-prev { left: 118px; }
  .arrow-next { left: 1054px; }
  .welcome-title { position: absolute; left: 175px; top: 690px; font-family: "Kalam", cursive; font-weight: 400; font-size: 34px; line-height: 44px; color: var(--teal); white-space: nowrap; }
  .welcome-text { position: absolute; left: 178px; top: 745px; width: 570px; font-size: 13px; line-height: 14.2px; color: var(--text); }
  .specials { position: absolute; left: 783px; top: 716px; width: 290px; height: 196px; background: var(--white); padding: 10px; box-shadow: 0 3px 8px rgba(0,0,0,0.2); }
  .specials-photo { width: 100%; height: 100%; background: linear-gradient(180deg, #6db3e6 0%, #e0508a 50%, #93c544 75%, #d8ceb5 100%); }
  .specials-tag {
    position: absolute; left: 905px; top: 703px; width: 152px; height: 38px;
    background: var(--orange); color: var(--white); text-align: center; line-height: 38px;
    font-family: "PT Sans Narrow", sans-serif; font-weight: 700; font-size: 13px; text-transform: uppercase;
    border-radius: 3px; box-shadow: 0 2px 4px rgba(0,0,0,0.2);
  }
  .bottom-line { position: absolute; left: 0; top: 946px; width: 1200px; height: 8px; background: var(--teal-light); }
  .bottom-band { position: absolute; left: 0; top: 960px; width: 1200px; height: 67px; background: var(--teal); }
</style>
</head>
<body>
  <div class="top-band"></div>

  <header>
    <div class="brand">
      <span class="brand-mark"></span>
      <span class="brand-name">Pelora Sands<br>Beach Suites</span>
    </div>
    <nav class="social" aria-label="Social links">
      <a href="#" aria-label="Quipster">QP</a>
      <a href="#" aria-label="Chatterly">CH</a>
      <a href="#" aria-label="Email">
        <svg width="20" height="14" viewBox="0 0 20 14"><rect x="1" y="1" width="18" height="12" fill="none" stroke="#fff" stroke-width="2"/><polyline points="1,1 10,8 19,1" fill="none" stroke="#fff" stroke-width="2"/></svg>
      </a>
    </nav>
    <div class="call">CALL US NOW<br>555-018-2046</div>
    <nav class="main-nav">
      <a class="nav-suites" href="#">Beachfront<br>Suites</a>
      <a class="nav-rates" href="#">Rates &amp;<br>Reservations</a>
      <a class="nav-gallery" href="#">Our<br>Gallery</a>
      <a class="nav-caye" href="#">All About<br>Caye Caulker</a>
      <a class="nav-contact" href="#">Contact<br>Us</a>
    </nav>
  </header>

  <section class="slider">
    <div class="slider-accent"></div>
    <div class="slider-frame">
      <div class="slider-photo" role="img" aria-label="Colourful pink, blue and lime beach suites with palm trees and lounge chairs on the sand"></div>
    </div>
    <svg class="arrow arrow-prev" viewBox="0 0 40 64"><path d="M40 0 A32 32 0 0 0 40 64 Z" fill="var(--orange)"/><polyline points="30,20 18,32 30,44" fill="none" stroke="#fff" stroke-width="4"/></svg>
    <svg class="arrow arrow-next" viewBox="0 0 40 64"><path d="M0 0 A32 32 0 0 1 0 64 Z" fill="var(--orange)"/><polyline points="10,20 22,32 10,44" fill="none" stroke="#fff" stroke-width="4"/></svg>
  </section>

  <section class="welcome">
    <h1 class="welcome-title">Welcome to a beautiful island escape</h1>
    <p class="welcome-text">Pelora Sands is located only fifty feet or so from the breathtaking Caribbean Sea on the tranquil island of Caye Caulker Belize with individual one-bedroom suites tastefully decorated to blend in with the island atmosphere. Each fully air-conditioned unit features either a king-sized bed or 2 queen-sized beds, private bath hot/cold water living room area cable flat screen TV, kitchenette and each has its own spacious deck space. Our ultra spacious units each with a approx. 500 sq ft of inside space makes them the most spacious yet affordable vacation units on the island. Warm furnishings make them a home away from home. This is the premier property on Caye Caulker. Come enjoy our breezy verandahs and starlit nights in relaxed comfort. Welcome to a beautiful island escape. These are beachfront condos that are among the best on the island. Step out from your deck and walk on the beach!</p>
  </section>

  <aside>
    <div class="specials">
      <div class="specials-photo" role="img" aria-label="Pink and lime beach suite by the palms"></div>
    </div>
    <a class="specials-tag" href="#">Click for specials</a>
  </aside>

  <div class="bottom-line"></div>
  <footer class="bottom-band"></footer>
</body>
</html>
```